Cover for novel by Dorian T. Velkam

I need a book cover for a young adult novel about a group of teenagers fleeing the repressive government of their home country pursued by cruel government agents. They must cross a river to reach a neighboring country where they will be safe. My idea is for a minimalist design, perhaps with a birds-eye view of a rowboat sitting in blue water with the oars crossed. The boat could be an abstract charcoal or pen-and-ink sketch. Of course, I'm open to ideas. Will need the front, spine, and back cover for hardback and paperback editions. Plus, the cover for eBook and audiobook versions. The book's title is: VELVET QUARRY, the author name is Dorian T. Velkam.

```html
<!DOCTYPE html>
<html lang="en">
<head>
<meta charset="utf-8">
<title>Velvet Quarry — Cover</title>
<link href="https://fonts.googleapis.com/css2?family=Bebas+Neue&display=swap" rel="stylesheet">
<style>
  :root {
    --stage: #20232b;
    --ghost-title: #3b1e25;
    --water: #86dcd7;
    --water-light: #9be6e1;
    --river-top: #d0141a;
    --river: #f20b0b;
    --title-red: #dd3340;
    --title-cyan: #2ff3f6;
    --author-red: #d42a36;
  }
  html, body {
    margin: 0;
    padding: 0;
    width: 1200px;
    height: 926px;
    overflow: hidden;
    background: var(--stage);
  }
  .stage {
    position: relative;
    width: 1200px;
    height: 926px;
    overflow: hidden;
    background: var(--stage);
  }
  .ghost-title {
    position: absolute;
    left: 0;
    top: 0;
    width: 1200px;
    height: 926px;
  }
  .ghost-title text {
    font-family: "Bebas Neue", "Oswald", sans-serif;
    fill: var(--ghost-title);
  }
  .book-cover {
    position: absolute;
    left: 349px;
    top: 62px;
    width: 502px;
    height: 803px;
    box-shadow: 0 18px 40px rgba(0, 0, 0, 0.55);
  }
  .book-cover svg { display: block; }
  .cover-text {
    font-family: "Bebas Neue", "Oswald", sans-serif;
  }
</style>
</head>
<body>
<div class="stage">
  <svg class="ghost-title" viewBox="0 0 1200 926" aria-hidden="true">
    <text x="4" y="1010" font-size="470" textLength="1192" lengthAdjust="spacingAndGlyphs">VELVET</text>
  </svg>

  <div class="book-cover">
    <svg width="502" height="803" viewBox="0 0 502 803" role="img" aria-label="Velvet Quarry by Dorian T. Velkam">
      <defs>
        <linearGradient id="water-tone" x1="0" y1="0" x2="0" y2="1">
          <stop offset="0" stop-color="var(--water-light)"/>
          <stop offset="1" stop-color="var(--water)"/>
        </linearGradient>
        <linearGradient id="river-tone" x1="0" y1="0" x2="0" y2="1">
          <stop offset="0" stop-color="var(--river-top)"/>
          <stop offset="1" stop-color="var(--river)"/>
        </linearGradient>
        <clipPath id="illustration-clip">
          <rect x="150" y="190" width="202" height="613" rx="24"/>
        </clipPath>
      </defs>

      <rect class="water" width="502" height="803" fill="url(#water-tone)"/>

      <text class="cover-text author-name" x="79" y="79" font-size="31" fill="var(--author-red)" textLength="348" lengthAdjust="spacing">DORIAN T. VELKAM</text>

      <rect class="illustration-area" x="150" y="190" width="202" height="613" rx="24" fill="url(#river-tone)" role="img" aria-label="Illustration: a rowboat with crossed oars seen from above, trailing a widening red river"/>

      <g class="title title-on-water cover-text" fill="var(--title-red)">
        <text x="6" y="474" font-size="164" textLength="490" lengthAdjust="spacingAndGlyphs">VELVET</text>
        <text x="56" y="592" font-size="160" textLength="390" lengthAdjust="spacingAndGlyphs">QUARRY</text>
      </g>
      <g class="title title-on-river cover-text" fill="var(--title-cyan)" clip-path="url(#illustration-clip)">
        <text x="6" y="474" font-size="164" textLength="490" lengthAdjust="spacingAndGlyphs">VELVET</text>
        <text x="56" y="592" font-size="160" textLength="390" lengthAdjust="spacingAndGlyphs">QUARRY</text>
      </g>
    </svg>
  </div>
</div>
</body>
</html>
```